Corkloft Soy Candles - New WP TEMPLATE

We make handemade soy candles in large volume and our company is now seeing huge growth, we are about to break into the retail market by providing our candles wholesale to retail outlets and gift stores.

Our candles are set apart by the fact they are very earth friendly in the sense of utilising old wine bottles that are cut in half and filling them with highly scented all natural pure soy and sealing the candle with a cork.

The website will need to be a complete Wordpress template. PLEASE ensure it is responsive and mobile friendly.

The look and feel of the website will need to be very original and rustic in feel.

Some examples of the "feel" of the site cand be found at the following links:

http://www.quarrymakers.example/blog/2011/07/new-website-launches-for-july/

http://www.pinerest7cabin.example/

http://www.vatglowwicks.example/

http://www.fern348.example/wedding-logo/rustic-ombre-summer-wedding-website/

http://plumthemes.example/grunge-website-design/screen-shot-2012-02-04-at-6-22-21-pm/

Our lettering logo is simply the word "Corkloft" in the font "Sweetly Broken". I have included our WORD logo and our SYMBOL logo. You will see our product in the images attached.

The site should include:

A slider
All images to be in circle cut outs (not square)

-A homepage with slider
-A section for "The Story" (This will be the largest page with a circle for each of the 6 scents and then a staggered story line of how we make the candles, alternating pictures from left to right).
-A section for "Retailers"
-A section for "Wholesale"
-A contact section

Please place some sort of placeholder images in all of the areas that will have images - were having the images done professionally and I have some design experience so I can finalise this aspect.

If you can make this a "One page template" that would be okay, but we are also open to multipage designs as long as its user friendly.

See images for the process and feel of product.

IF you think the prize needs to be increased and you have a good design that we like, we are happy to negotiate with you!

Industry/Entity Type

Retail

```html
<!DOCTYPE html>
<html lang="en">
<head>
<meta charset="utf-8">
<title>Corkloft Soy Candles</title>
<link rel="stylesheet" href="https://fonts.googleapis.com/css2?family=Rokkitt:wght@400;500&family=Roboto+Condensed:wght@400;500&family=Raleway:wght@400;700&display=swap">
<style>
  :root {
    --brown: #8a4916;
    --brown-dark: #6b3310;
    --cream: #f3e1a8;
    --paper: #ebe7df;
    --paper-top: #e3dfd6;
    --gold: #c8a558;
    --gold-light: #f0dea2;
    --ink: #2c2620;
    --text: #3a342e;
    --nav-text: #f6e7cc;
    --white: #ffffff;
  }
  * { margin: 0; padding: 0; box-sizing: border-box; }
  html, body { width: 1056px; height: 1200px; overflow: hidden; background: var(--paper); }
  .page { position: relative; width: 1056px; height: 1200px; overflow: hidden; background: var(--paper); font-family: "Roboto Condensed", sans-serif; color: var(--text); }

  .site-header { position: absolute; left: 0; top: 0; width: 1056px; height: 44px; background: var(--brown); border-bottom: 4px solid #f5f2ec; z-index: 3; }
  .brand-tab { position: absolute; left: 88px; top: 0; width: 262px; height: 121px; background: var(--cream); clip-path: polygon(0 0, 92% 0, 100% 100%, 9% 100%); z-index: 4; display: flex; align-items: center; justify-content: center; }
  .brand-name { font-family: "Rokkitt", serif; font-weight: 400; font-size: 44px; color: #7a3f16; padding-left: 14px; }
  .main-nav { position: absolute; top: 0; left: 340px; height: 40px; display: flex; align-items: center; }
  .main-nav a { font-family: "Rokkitt", serif; font-size: 14px; letter-spacing: 0.5px; color: var(--nav-text); text-decoration: none; padding: 0 22px; line-height: 26px; border-right: 1px solid #a76231; }
  .main-nav a:last-child { border-right: none; }
  .cart-tab { position: absolute; left: 815px; top: 0; width: 153px; height: 35px; background: var(--cream); clip-path: polygon(0 0, 100% 0, 100% 100%, 9% 100%); display: flex; align-items: center; justify-content: flex-end; gap: 8px; padding-right: 10px; font-family: "Rokkitt", serif; font-size: 13px; color: #6a4222; }

  .hero-band { position: absolute; left: 0; top: 44px; width: 1056px; height: 458px; background: var(--paper-top); border-bottom: 1px solid #d8d3c9; }
  .slider-frame { position: absolute; left: 90px; top: 73px; width: 878px; height: 396px; background: #f4f2ed; box-shadow: 0 1px 3px rgba(0,0,0,0.12); }
  .slide-image { position: absolute; left: 9px; top: 10px; width: 858px; height: 376px; background: linear-gradient(180deg, #cfd3c7 0%, #b9b79a 30%, #8d8a55 55%, #5d3b2d 85%, #3f2a22 100%); }
  .slide-caption { position: absolute; left: 0; bottom: 0; width: 100%; height: 60px; background: rgba(30,26,24,0.82); color: var(--white); font-size: 30px; text-align: center; line-height: 60px; letter-spacing: 0.5px; }
  .slider-arrow { position: absolute; top: 218px; width: 44px; height: 44px; }
  .slider-arrow.prev { left: 29px; }
  .slider-arrow.next { left: 983px; }

  .section-banner { position: absolute; left: 92px; top: 525px; width: 872px; height: 60px; border-radius: 4px; background: linear-gradient(90deg, var(--gold) 0%, var(--gold-light) 50%, var(--gold) 100%); display: flex; align-items: center; justify-content: center; gap: 10px; }
  .section-banner h2 { font-family: "Rokkitt", serif; font-weight: 400; font-size: 38px; color: var(--ink); letter-spacing: 1.5px; }

  .feature { position: absolute; top: 632px; width: 280px; text-align: center; }
  .feature-icon { width: 100px; height: 95px; margin: 0 auto; background: #f1eee8; border-radius: 6px; box-shadow: 0 1px 4px rgba(0,0,0,0.15); display: flex; align-items: center; justify-content: center; }
  .feature h3 { margin-top: 20px; font-weight: 500; font-size: 20px; color: var(--ink); letter-spacing: 0.5px; }
  .feature p { margin-top: 12px; font-size: 12.5px; line-height: 21px; letter-spacing: 0.3px; }
  .feature.contact p { margin-top: 12px; line-height: 17.5px; }
  .retailers { left: 92px; }
  .wholesale { left: 388px; }
  .contact { left: 689px; }
  .col-divider { position: absolute; top: 634px; width: 1px; height: 215px; background: #d9d4ca; }

  .site-footer { position: absolute; left: 0; top: 938px; width: 1056px; height: 222px; background: var(--brown); color: var(--white); }
  .site-footer h4 { font-family: "Raleway", sans-serif; font-weight: 700; font-size: 19px; }
  .testimonials { position: absolute; left: 106px; top: 40px; width: 250px; }
  .testimonials p { margin-top: 12px; font-family: "Raleway", sans-serif; font-size: 12px; line-height: 17px; }
  .service-list { position: absolute; left: 419px; top: 37px; width: 280px; }
  .service-item { display: flex; gap: 15px; margin-top: 16px; }
  .service-item:first-of-type { margin-top: 14px; }
  .service-thumb { width: 62px; height: 51px; flex: none; }
  .service-item p { font-family: "Raleway", sans-serif; font-size: 12px; line-height: 16px; margin-top: 2px; }
  .footer-brand { position: absolute; left: 760px; top: 80px; width: 150px; text-align: center; font-family: "Raleway", sans-serif; font-weight: 400; font-size: 34px; color: var(--white); }
  .copyright { position: absolute; left: 0; top: 1160px; width: 1056px; height: 40px; background: var(--brown-dark); color: #dcc2a2; font-family: "Raleway", sans-serif; font-size: 12px; text-align: center; line-height: 38px; }
</style>
</head>
<body>
<div class="page">
  <header class="site-header">
    <nav class="main-nav">
      <a href="#">HOME</a>
      <a href="#">ABOUT US</a>
      <a href="#">SERVICES</a>
      <a href="#">CONTACT US</a>
    </nav>
    <div class="cart-tab">Shopping Cart
      <svg width="22" height="20" viewBox="0 0 22 20" fill="none" stroke="#6a4222" stroke-width="1.4">
        <path d="M1 2h3l3 11h11l2-8H6"/><circle cx="9" cy="17" r="1.5"/><circle cx="16" cy="17" r="1.5"/>
        <path d="M8 8h11M9 10.5h9"/>
      </svg>
    </div>
  </header>
  <div class="brand-tab"><span class="brand-name">Corkloft</span></div>

  <section class="hero-band">
    <svg class="slider-arrow prev" viewBox="0 0 44 44"><circle cx="22" cy="22" r="20.5" fill="none" stroke="#111" stroke-width="2.5"/><path d="M25 13l-9 9 9 9" fill="none" stroke="#111" stroke-width="3"/></svg>
    <svg class="slider-arrow next" viewBox="0 0 44 44"><circle cx="22" cy="22" r="20.5" fill="none" stroke="#111" stroke-width="2.5"/><path d="M19 13l9 9-9 9" fill="none" stroke="#111" stroke-width="3"/></svg>
    <div class="slider-frame">
      <div class="slide-image" role="img" aria-label="Photo of soy candles poured into cut wine bottles with cream labels, standing on a granite bench">
        <div class="slide-caption">WELCOME TO CORKLOFT</div>
      </div>
    </div>
  </section>

  <div class="section-banner">
    <svg width="150" height="12" viewBox="0 0 150 12"><line x1="30" y1="6" x2="150" y2="6" stroke="#7a3a12" stroke-width="1.5"/><circle cx="30" cy="6" r="3" fill="#7a3a12"/></svg>
    <h2>A SECTION</h2>
    <svg width="150" height="12" viewBox="0 0 150 12"><line x1="0" y1="6" x2="120" y2="6" stroke="#7a3a12" stroke-width="1.5"/><circle cx="120" cy="6" r="3" fill="#7a3a12"/></svg>
  </div>

  <div class="col-divider" style="left:389px"></div>
  <div class="col-divider" style="left:680px"></div>

  <article class="feature retailers">
    <div class="feature-icon">
      <svg width="70" height="62" viewBox="0 0 70 62" fill="#c9a255">
        <path d="M20 20L30 4h4L25 20zM50 20L40 4h-4l9 16z"/>
        <rect x="2" y="18" width="66" height="8" rx="2"/>
        <path d="M7 28h56l-6 30H13z"/>
        <g fill="#f1eee8"><rect x="17" y="32" width="9" height="8"/><rect x="30" y="32" width="10" height="8"/><rect x="44" y="32" width="9" height="8"/><rect x="18" y="44" width="8" height="8"/><rect x="30" y="44" width="10" height="8"/><rect x="44" y="44" width="8" height="8"/></g>
      </svg>
    </div>
    <h3>RETAILERS</h3>
    <p>Our ad servers are integrated with 3rd party software which provides domain transpar-ency and brand protection, preventing ads from displaying where they shouldn't.</p>
  </article>

  <article class="feature wholesale">
    <div class="feature-icon">
      <svg width="56" height="60" viewBox="0 0 56 60" fill="#c9a255">
        <rect x="2" y="16" width="30" height="28" rx="3"/>
        <rect x="10" y="10" width="14" height="8" rx="2" fill="none" stroke="#c9a255" stroke-width="3"/>
        <path d="M38 46V8a4 4 0 0 1 4-4h10v5h-9v37z"/>
        <rect x="2" y="44" width="40" height="4"/>
        <circle cx="10" cy="54" r="5"/><circle cx="34" cy="54" r="5"/>
      </svg>
    </div>
    <h3>WHOLESALE</h3>
    <p>We can integrate with most ad servers for both advertisers and publishers through an API in order to maximize the revenue po-tential of each ad call.</p>
  </article>

  <article class="feature contact">
    <div class="feature-icon">
      <svg width="66" height="60" viewBox="0 0 66 60" fill="#c9a255">
        <path d="M6 16c0-5 5-9 9-8l6 10-5 5c2 7 9 14 16 17l5-5 10 6c1 4-3 9-8 9C20 50 6 34 6 16z"/>
        <path d="M36 4h22a6 6 0 0 1 6 6v12a6 6 0 0 1-6 6H46l-8 6 2-6h-4a6 6 0 0 1-6-6V10a6 6 0 0 1 6-6z"/>
        <g fill="#f1eee8"><circle cx="40" cy="16" r="2.5"/><circle cx="47" cy="16" r="2.5"/><circle cx="54" cy="16" r="2.5"/></g>
      </svg>
    </div>
    <h3>CONTACT US</h3>
    <p>D-40000 Lindenfeld<br>Halden Phone: +49 (0) 2100/55501<br>village square 1 Talbach A-6000<br>Austria Phone: +43 (0) 5200 55502<br>Fax: +43 (0) 5200 55503</p>
  </article>

  <footer class="site-footer">
    <div class="testimonials">
      <h4>Our Customers Say:</h4>
      <p>Lorem Ipsum is simply dummy text of the printing and typesetting industry. Lorem Ipsum has been the industry's standard dummy text ever since the 1500s, when an unknown printer took a galley of type and scrambled it to make a type specimen book. It has survived not only five centuries,</p>
    </div>
    <div class="service-list">
      <h4>All Services</h4>
      <div class="service-item">
        <div class="service-thumb" role="img" aria-label="Photo of green wine bottle candles" style="background:linear-gradient(160deg,#d8dcd2,#8fa06a 60%,#4d5d3a)"></div>
        <p>Lorem Ipsum is simply dummy text of the printing and typeset-ting industry.</p>
      </div>
      <div class="service-item">
        <div class="service-thumb" role="img" aria-label="Photo of rows of finished candles on a workbench" style="background:linear-gradient(180deg,#c8b8a4,#a7794f 55%,#6d4428)"></div>
        <p>Lorem Ipsum is simply dummy text of the printing and typeset-ting industry.</p>
      </div>
    </div>
    <div class="footer-brand">Corkloft</div>
  </footer>
  <div class="copyright">© 2014 Copyright - Corkloft . All rights reserved</div>
</div>
</body>
</html>
```